Velvette by Marisa Holt business cards

I am after a business card that will fit the name of my business - velvette.
I want something classy and sexy and nothing tacky.
Ideas that I like are Zebra print backgrounds glitter back grounds
Two ideas I had were
1. Zebra print in black and white, the name Velvette by Marisa Holt and a shilouette of a woman laying on top of the name. Or instead of zebra a glitter background.
2. Idea very similar except for instead of a woman a pair of lips maybe a hot pink glitter or a gold glitter depending on background with the business name between the lips.
Or you can do something completely different.

Industry/Entity Type

Business

```html
<!DOCTYPE html>
<html lang="en">
<head>
<meta charset="utf-8">
<title>Velvette by Marisa Holt – Business Cards</title>
<link rel="stylesheet" href="https://fonts.googleapis.com/css2?family=Cinzel:wght@400;600&family=Open+Sans:wght@400;600&family=Roboto+Condensed:wght@400&display=swap">
<style>
  :root {
    --bg: #2a2a2a;
    --print-dark: #6a6a6a;
    --print-light: #a2a2a2;
    --purple-top: #9a5cc6;
    --purple-mid: #8448b0;
    --purple-deep: #5f2c86;
    --silver: #ececf2;
    --silver-soft: #d9d3e4;
    --ink-light: #ffffff;
  }
  * { margin: 0; padding: 0; box-sizing: border-box; }
  html, body { width: 1200px; height: 900px; overflow: hidden; }
  body {
    background: var(--bg);
    font-family: "Open Sans", sans-serif;
    position: relative;
  }
  .card {
    position: absolute;
    left: 320px;
    width: 560px;
    height: 320px;
    overflow: hidden;
    box-shadow: 0 10px 30px rgba(0,0,0,.5);
  }
  .card--back { top: 100px; }
  .card--front { top: 480px; }

  .print-area {
    position: absolute;
    inset: 0;
    background: linear-gradient(135deg, var(--print-light) 0%, var(--print-dark) 100%);
  }

  /* Back side */
  .brand-panel {
    position: absolute;
    left: 44px; top: 32px; right: 26px; bottom: 38px;
    border-radius: 24px;
    background: linear-gradient(180deg, var(--purple-deep) 0%, var(--purple-mid) 18%, var(--purple-top) 60%, var(--purple-mid) 100%);
    box-shadow: inset 0 14px 22px rgba(0,0,0,.45);
    display: flex;
    flex-direction: column;
    align-items: center;
    justify-content: center;
  }
  .brand-figure {
    width: 46px; height: 62px;
    border-radius: 20px 20px 6px 6px;
    background: linear-gradient(180deg, var(--silver), var(--silver-soft));
    margin-bottom: 4px;
  }
  .brand-name {
    font-family: "Cinzel", serif;
    font-weight: 400;
    font-size: 50px;
    letter-spacing: 3px;
    color: var(--silver);
    line-height: 1;
  }
  .brand-web {
    font-family: "Open Sans", sans-serif;
    font-size: 20px;
    letter-spacing: 1px;
    color: var(--silver);
    margin-top: 6px;
  }

  /* Front side */
  .contact-panel {
    position: absolute;
    left: 0; top: 50px;
    width: 270px; height: 232px;
    border-radius: 0 22px 0 0;
    background: linear-gradient(180deg, var(--purple-top) 0%, var(--purple-mid) 100%);
  }
  .holder-name {
    position: absolute;
    left: 18px; top: 14px;
    font-family: "Cinzel", serif;
    font-size: 24px;
    font-weight: 400;
    line-height: 1.2;
    color: var(--ink-light);
    letter-spacing: 1px;
    white-space: nowrap;
  }
  .holder-role {
    position: absolute;
    left: 20px; top: 48px;
    font-size: 15px;
    font-weight: 600;
    color: var(--silver-soft);
  }
  .contact-list {
    position: absolute;
    left: 20px; top: 78px;
    list-style: none;
    font-family: "Roboto Condensed", sans-serif;
    font-size: 15px;
    color: var(--silver-soft);
  }
  .contact-list li {
    display: flex;
    align-items: center;
    gap: 22px;
    height: 24px;
  }
  .contact-list svg { width: 16px; height: 14px; flex: none; }
  .holder-figure {
    position: absolute;
    right: 14px; top: 64px;
    width: 70px; height: 158px;
    border-radius: 30px 30px 8px 8px;
    background: linear-gradient(180deg, var(--ink-light), var(--silver-soft));
  }
  .front-brand {
    position: absolute;
    left: 56px; bottom: 14px;
    font-family: "Cinzel", serif;
    font-size: 20px;
    letter-spacing: 2px;
    line-height: 1.2;
    color: var(--silver);
  }
</style>
</head>
<body>

  <section class="card card--back">
    <div class="print-area" role="img" aria-label="Black and white zebra print background"></div>
    <div class="brand-panel">
      <div class="brand-figure" role="img" aria-label="Silhouette of a woman"></div>
      <div class="brand-name">Velvette</div>
      <div class="brand-web">yourwebsite.com</div>
    </div>
  </section>

  <section class="card card--front">
    <div class="print-area" role="img" aria-label="Black and white zebra print background"></div>
    <div class="contact-panel">
      <div class="holder-name">Marisa Holt</div>
      <div class="holder-role">Designation</div>
      <ul class="contact-list">
        <li>
          <svg viewBox="0 0 16 14" aria-hidden="true"><path d="M2 5c0-3 12-3 12 0l-3 1-1-2H6L5 6z M4 7h8l2 6H2z" fill="#e6e0ee"/></svg>
          <span>Phone Number</span>
        </li>
        <li>
          <svg viewBox="0 0 16 14" aria-hidden="true"><rect x="1" y="2" width="14" height="10" fill="#e6e0ee"/><path d="M1 2l7 6 7-6" fill="none" stroke="#8448b0" stroke-width="1.2"/></svg>
          <span>E-mail Address</span>
        </li>
        <li>
          <svg viewBox="0 0 16 14" aria-hidden="true"><g fill="none" stroke="#e6e0ee" stroke-width="1.2"><circle cx="8" cy="7" r="6"/><ellipse cx="8" cy="7" rx="2.6" ry="6"/><path d="M2 7h12"/></g></svg>
          <span>Website</span>
        </li>
      </ul>
      <div class="holder-figure" role="img" aria-label="Silhouette of a woman"></div>
      <div class="front-brand">Velvette</div>
    </div>
  </section>

</body>
</html>
```